Civic Learning Studio PocketDeck

We are looking for a fresh new look for our famous Signal Sense Handset cards. These cards are used as a pedagogical device by teachers and students to help people critically analyze media messages.

Now that we are in the era of Orvo 12, we would like the Signal Sense Handset to look fresh and new. All the content stays the same, but graphic elements, color and overall design can be changed to look contemporary and modern.

Target Market(s)

Teenagers, young adults, secondary and college teachers

Industry/Entity Type

Education

Colors

Designer to choose colors to be used in the design.

Requirements
Must have
• All the content that is on the current card, with icons and text
Nice to have
• Fresh use of color
• More modern phone design like the smartphones people use today
Should not have
• ...too much black

```html
<!DOCTYPE html>
<html lang="en">
<head>
<meta charset="utf-8">
<title>Civic Learning Studio – Time to Discuss Postcard</title>
<link rel="stylesheet" href="https://fonts.googleapis.com/css2?family=Oswald:wght@400;500;600&family=Itim&family=Roboto:wght@500;700&display=swap">
<style>
:root{
  --teal:#1aa0b8;
  --green:#8cc63f;
  --orange:#f15a29;
  --yellow:#f7c21b;
  --ink:#222222;
  --paper:#ffffff;
  --page:#e8e5e1;
  --rule:#555555;
  --phone:#111111;
}
*{box-sizing:border-box;margin:0;padding:0}
html,body{width:960px;height:1200px;overflow:hidden;background:var(--page)}
body{position:relative;font-family:"Itim",sans-serif;color:var(--ink)}
.card{position:absolute;left:115px;width:861px;height:660px;background:var(--paper);transform:scale(.848);transform-origin:top left;overflow:hidden;box-shadow:0 6px 18px rgba(0,0,0,.18)}
.card--front{top:25px}
.card--back{top:615px;height:663px}
.abs{position:absolute}
svg.defs{position:absolute;width:0;height:0}

/* brand */
.brand{position:absolute;display:flex;flex-direction:column;align-items:center}
.brand__row{display:flex;align-items:center;gap:12px}
.brand__mark{width:30px;height:30px;background:var(--teal);border-radius:4px;flex:none}
.brand__name{font-family:"Oswald",sans-serif;font-weight:500;font-size:38px;color:var(--ink);line-height:1.1;white-space:nowrap}
.url{font-family:"Oswald",sans-serif;color:var(--ink);white-space:nowrap}
.url b{color:var(--teal);font-weight:inherit}
.brand .url{font-size:17px;margin-top:4px}
.brand--back{left:24px;top:452px;width:290px}
.brand--back .brand__row{gap:10px}
.brand--back .brand__mark{width:26px;height:26px}
.brand--back .brand__name{font-size:27px}
.brand--back .url{font-size:14px}

/* front */
.band-teal{left:0;top:198px;width:861px;height:232px;background:var(--teal)}
.band-green{left:0;top:430px;width:861px;height:175px;background:var(--green)}
.tab{left:0;top:186px;width:268px;height:50px;background:var(--orange);border-radius:0 6px 6px 0;color:#fff;font-family:"Oswald",sans-serif;font-weight:600;font-size:28px;line-height:50px;padding-left:36px;letter-spacing:.5px}
.list{position:absolute;display:grid;list-style:none;color:#fff;font-size:17px}
.list li{display:flex;align-items:center;gap:20px;white-space:nowrap}
.list--prompts{left:30px;top:262px;grid-template-columns:275px 300px;grid-auto-flow:column;grid-template-rows:repeat(4,40px)}
.list--media{left:30px;top:448px;grid-template-columns:155px 165px 150px;grid-auto-flow:column;grid-template-rows:repeat(4,36.7px)}
.chip{width:28px;height:28px;background:#fff;border-radius:5px;display:flex;align-items:center;justify-content:center;flex:none}
.chip svg{width:20px;height:20px;color:var(--ink)}
.footer-url{left:0;top:605px;width:861px;height:55px;text-align:center;font-size:40px;line-height:55px}

/* phone */
.phone{left:560px;top:23px;width:283px;height:572px;border:9px solid var(--phone);border-radius:44px;background:var(--phone);overflow:hidden}
.phone__screen{position:absolute;inset:0;border-radius:34px;background:linear-gradient(160deg,#7a6a4a 0%,#5b4e3c 40%,#3f4a3a 70%,#2c2c2c 100%)}
.phone__notch{position:absolute;left:50%;top:0;width:120px;height:22px;margin-left:-60px;background:var(--phone);border-radius:0 0 14px 14px}
.phone__title{position:absolute;left:0;right:0;top:58px;height:36px;background:rgba(0,0,0,.35);border-top:1px solid rgba(255,255,255,.6);border-bottom:1px solid rgba(255,255,255,.6);color:#fff;text-align:center;font-family:"Roboto",sans-serif;font-weight:700;font-size:22px;line-height:34px}
.apps{position:absolute;left:0;top:118px;width:265px;display:grid;grid-template-columns:repeat(4,66px);grid-template-rows:88px 112px 77px 77px 77px}
.app{display:flex;flex-direction:column;align-items:center;color:#fff;font-family:"Roboto",sans-serif;font-weight:700;font-size:9px;line-height:1.15;text-align:center}
.app__icon{width:46px;height:46px;border-radius:8px;background:#fff;display:flex;align-items:center;justify-content:center;margin-bottom:4px;color:var(--ink)}
.app__icon svg{width:30px;height:30px}
.app__icon--teal{background:var(--teal);color:#fff}
.app__icon--green{background:var(--green);color:#fff}
.app__icon--yellow{background:var(--yellow);color:#fff}
.app__icon--orange{background:var(--orange);color:#fff}

/* back */
.questions-panel{left:0;top:0;width:461px;height:563px;border:1px solid #d7e8c2;border-top:none}
.questions-head{left:0;top:0;width:461px;height:77px;background:var(--green);color:#fff;font-family:"Oswald",sans-serif;font-weight:500;font-size:28px;line-height:80px;padding-left:34px}
.questions{position:absolute;left:23px;top:90px;width:440px;list-style:none;font-size:17px;line-height:21.5px}
.questions li{display:flex;gap:14px;margin-bottom:15px}
.tick{width:16px;height:16px;background:var(--teal);border-radius:3px;flex:none;margin-top:3px;display:flex;align-items:center;justify-content:center}
.tick svg{width:13px;height:13px;color:#fff}
.stamp{left:700px;top:43px;width:116px;height:142px;border:1px solid var(--rule)}
.addr-line{left:551px;width:265px;height:1px;background:var(--rule)}
.mini-phone{left:325px;top:285px;width:130px;height:265px;border:5px solid var(--phone);border-radius:14px;background:#1e1e1e;overflow:hidden;font-family:"Roboto",sans-serif;color:#fff}
.mini-phone__title{text-align:center;font-weight:700;font-size:8.5px;line-height:9px;margin-top:25px;padding-bottom:5px;border-bottom:1px solid #777}
.mini-q{display:flex;margin:5px 4px 0;font-size:6px;line-height:6.5px;font-weight:500;color:var(--ink)}
.mini-q span{width:9px;flex:none;color:#fff;background:var(--teal);text-align:center;padding-top:1px}
.mini-q p{flex:1;padding:2px 3px;background:#cfeef4}
.mini-q--2 span{background:var(--green)} .mini-q--2 p{background:#e4f2cf}
.mini-q--3 span{background:var(--yellow)} .mini-q--3 p{background:#fcefc0}
.mini-q--4 span{background:var(--orange)} .mini-q--4 p{background:#fbd9cc}
.mini-phone__brand{position:absolute;left:0;right:0;bottom:12px;text-align:center;font-size:7px;font-weight:700}
.mini-phone__brand small{display:block;font-size:4.5px;font-weight:500;color:#bbb}
</style>
</head>
<body>

<svg class="defs" aria-hidden="true">
  <defs>
    <symbol id="i-tick" viewBox="0 0 24 24"><path d="M4 12.5l5 5L20 6" fill="none" stroke="currentColor" stroke-width="3.2" stroke-linecap="round" stroke-linejoin="round"/></symbol>
    <symbol id="i-bag" viewBox="0 0 24 24"><path d="M9 3h6l-2 4h-2z" fill="currentColor"/><circle cx="12" cy="15" r="7" fill="currentColor"/><text x="12" y="19" text-anchor="middle" font-size="10" font-family="Arial" font-weight="700" fill="#fff">$</text></symbol>
    <symbol id="i-q" viewBox="0 0 24 24"><text x="12" y="20" text-anchor="middle" font-size="21" font-family="Arial" font-weight="700" fill="currentColor">?</text></symbol>
    <symbol id="i-gem" viewBox="0 0 24 24"><path d="M3 9l4-5h10l4 5-9 12z M3 9h18 M9 4l3 5 3-5 M12 9v12" fill="none" stroke="currentColor" stroke-width="1.8" stroke-linejoin="round"/></symbol>
    <symbol id="i-eye" viewBox="0 0 24 24"><path d="M2 12s4-6 10-6 10 6 10 6-4 6-10 6S2 12 2 12z" fill="none" stroke="currentColor" stroke-width="2"/><circle cx="12" cy="12" r="3.2" fill="currentColor"/></symbol>
    <symbol id="i-bell" viewBox="0 0 24 24"><path d="M6 17V11a6 6 0 0 1 12 0v6l2 2H4z" fill="currentColor"/><circle cx="12" cy="21" r="2" fill="currentColor"/></symbol>
    <symbol id="i-warn" viewBox="0 0 24 24"><path d="M12 3L22 21H2z" fill="currentColor"/><path d="M12 9v6" stroke="#fff" stroke-width="2.2"/><circle cx="12" cy="18" r="1.2" fill="#fff"/></symbol>
    <symbol id="i-pencil" viewBox="0 0 24 24"><path d="M5 19l1-4L16 5l3 3L9 18z" fill="currentColor"/><path d="M4 21h16" stroke="currentColor" stroke-width="2"/></symbol>
    <symbol id="i-news" viewBox="0 0 24 24"><rect x="3" y="5" width="18" height="14" rx="1" fill="none" stroke="currentColor" stroke-width="2"/><rect x="6" y="8" width="5" height="4" fill="currentColor"/><path d="M13 9h5M13 12h5M6 15h12" stroke="currentColor" stroke-width="1.6"/></symbol>
    <symbol id="i-share" viewBox="0 0 24 24"><path d="M17 6L7 12l10 6" fill="none" stroke="currentColor" stroke-width="2"/><circle cx="17" cy="6" r="3" fill="currentColor"/><circle cx="7" cy="12" r="3" fill="currentColor"/><circle cx="17" cy="18" r="3" fill="currentColor"/></symbol>
    <symbol id="i-clap" viewBox="0 0 24 24"><rect x="4" y="10" width="16" height="10" fill="currentColor"/><path d="M4 9l15-4 1 3-15 4z" fill="currentColor"/></symbol>
    <symbol id="i-book" viewBox="0 0 24 24"><rect x="6" y="3" width="12" height="18" rx="1.5" fill="currentColor"/><path d="M8 5v14" stroke="#fff" stroke-width="1"/></symbol>
    <symbol id="i-pad" viewBox="0 0 24 24"><path d="M7 8h10a4 4 0 0 1 4 4l1 5a2 2 0 0 1-3.5 1.5L16 16H8l-2.5 2.5A2 2 0 0 1 2 17l1-5a4 4 0 0 1 4-4z" fill="currentColor"/><path d="M7 10v4M5 12h4" stroke="#fff" stroke-width="1.4"/><circle cx="16" cy="11" r="1" fill="#fff"/><circle cx="18" cy="13" r="1" fill="#fff"/></symbol>
    <symbol id="i-pod" viewBox="0 0 24 24"><circle cx="12" cy="11" r="2.5" fill="currentColor"/><path d="M8 15a5 5 0 1 1 8 0M5.5 17.5a8.5 8.5 0 1 1 13 0" fill="none" stroke="currentColor" stroke-width="1.8"/><path d="M12 14v7" stroke="currentColor" stroke-width="2"/></symbol>
    <symbol id="i-note" viewBox="0 0 24 24"><path d="M9 17V5l11-2v12" fill="none" stroke="currentColor" stroke-width="2"/><circle cx="6.5" cy="17.5" r="3" fill="currentColor"/><circle cx="17.5" cy="15.5" r="3" fill="currentColor"/></symbol>
    <symbol id="i-apps" viewBox="0 0 24 24"><rect x="6" y="2" width="12" height="20" rx="2" fill="none" stroke="currentColor" stroke-width="1.8"/><path d="M9 7h2v2H9zM13 7h2v2h-2zM9 11h2v2H9zM13 11h2v2h-2z" fill="currentColor"/></symbol>
    <symbol id="i-comic" viewBox="0 0 24 24"><path d="M3 5h18v11H10l-5 4v-4H3z" fill="currentColor"/><circle cx="8" cy="10.5" r="1.3" fill="#fff"/><circle cx="12" cy="10.5" r="1.3" fill="#fff"/><circle cx="16" cy="10.5" r="1.3" fill="#fff"/></symbol>
    <symbol id="i-globe" viewBox="0 0 24 24"><circle cx="12" cy="12" r="9" fill="none" stroke="currentColor" stroke-width="1.8"/><ellipse cx="12" cy="12" rx="4" ry="9" fill="none" stroke="currentColor" stroke-width="1.5"/><path d="M3 12h18M5 7h14M5 17h14" stroke="currentColor" stroke-width="1.3"/></symbol>
    <symbol id="i-tv" viewBox="0 0 24 24"><rect x="3" y="7" width="18" height="12" rx="1" fill="none" stroke="currentColor" stroke-width="2"/><path d="M8 3l4 4 4-4M8 22h8" stroke="currentColor" stroke-width="1.8" fill="none"/></symbol>
    <symbol id="i-power" viewBox="0 0 24 24"><path d="M7 6.5a8 8 0 1 0 10 0" fill="none" stroke="currentColor" stroke-width="2.4" stroke-linecap="round"/><path d="M12 3v9" stroke="currentColor" stroke-width="2.4" stroke-linecap="round"/></symbol>
    <symbol id="i-tablet" viewBox="0 0 24 24"><rect x="5" y="3" width="14" height="18" rx="2" fill="none" stroke="currentColor" stroke-width="2.2"/><circle cx="12" cy="18.5" r="1" fill="currentColor"/></symbol>
    <symbol id="i-radio" viewBox="0 0 24 24"><rect x="3" y="8" width="18" height="13" rx="1.5" fill="currentColor"/><path d="M6 8l10-5" stroke="currentColor" stroke-width="1.6"/><circle cx="8" cy="15" r="3" fill="#fff"/><path d="M14 13h5M14 16h5" stroke="#fff" stroke-width="1.5"/></symbol>
  </defs>
</svg>

<!-- FRONT -->
<section class="card card--front" aria-label="Postcard front: Time to Discuss">
  <div class="brand" style="left:55px;top:52px">
    <div class="brand__row"><span class="brand__mark"></span><span class="brand__name">Civic Learning Studio</span></div>
    <div class="url">www.<b>civiclearningstudio</b>.org</div>
  </div>

  <div class="abs band-teal"></div>
  <div class="abs band-green"></div>
  <div class="abs tab">TIME TO DISCUSS</div>

  <ul class="list list--prompts">
    <li><span class="chip"><svg><use href="#i-tick"/></svg></span>Reality Check</li>
    <li><span class="chip"><svg><use href="#i-bag"/></svg></span>Private Gain or Public Good?</li>
    <li><span class="chip"><svg><use href="#i-q"/></svg></span>What's Left Out?</li>
    <li><span class="chip"><svg><use href="#i-gem"/></svg></span>Values Check</li>
    <li><span class="chip"><svg><use href="#i-eye"/></svg></span>Read Between the Lines</li>
    <li><span class="chip"><svg><use href="#i-bell"/></svg></span>Stereotype Alert</li>
    <li><span class="chip"><svg><use href="#i-warn"/></svg></span>Solutions too Easy</li>
    <li><span class="chip"><svg><use href="#i-pencil"/></svg></span>Record/Save for Later</li>
  </ul>

  <ul class="list list--media">
    <li><span class="chip"><svg><use href="#i-news"/></svg></span>News Media</li>
    <li><span class="chip"><svg><use href="#i-book"/></svg></span>Books</li>
    <li><span class="chip"><svg><use href="#i-note"/></svg></span>Music</li>
    <li><span class="chip"><svg><use href="#i-globe"/></svg></span>Websites</li>
    <li><span class="chip"><svg><use href="#i-share"/></svg></span>Social Media</li>
    <li><span class="chip"><svg><use href="#i-pad"/></svg></span>Video Games</li>
    <li><span class="chip"><svg><use href="#i-apps"/></svg></span>Apps</li>
    <li><span class="chip"><svg><use href="#i-tv"/></svg></span>TV</li>
    <li><span class="chip"><svg><use href="#i-clap"/></svg></span>Movies</li>
    <li><span class="chip"><svg><use href="#i-pod"/></svg></span>Podcasts</li>
    <li><span class="chip"><svg><use href="#i-comic"/></svg></span>Comics</li>
    <li><span class="chip"><svg><use href="#i-power"/></svg></span>Off</li>
  </ul>

  <div class="abs phone">
    <div class="phone__screen" role="img" aria-label="Photo of a group of smiling teenagers as the phone wallpaper"></div>
    <div class="phone__notch"></div>
    <div class="phone__title">TIME TO DISCUSS</div>
    <div class="apps">
      <div class="app"><span class="app__icon app__icon--teal"><svg><use href="#i-tick"/></svg></span>Reality<br>Check</div>
      <div class="app"><span class="app__icon app__icon--green"><svg><use href="#i-bag"/></svg></span>Private Gain or<br>Public Good?</div>
      <div class="app"><span class="app__icon app__icon--yellow"><svg><use href="#i-q"/></svg></span>What's<br>Left Out?</div>
      <div class="app"><span class="app__icon app__icon--orange"><svg><use href="#i-gem"/></svg></span>Values<br>Check</div>
      <div class="app"><span class="app__icon app__icon--orange"><svg><use href="#i-eye"/></svg></span>Read Between<br>the Lines</div>
      <div class="app"><span class="app__icon app__icon--yellow"><svg><use href="#i-bell"/></svg></span>Stereotype<br>Alert</div>
      <div class="app"><span class="app__icon app__icon--green"><svg><use href="#i-warn"/></svg></span>Solutions<br>too Easy</div>
      <div class="app"><span class="app__icon app__icon--teal"><svg><use href="#i-pencil"/></svg></span>Record/Save<br>for Later</div>
      <div class="app"><span class="app__icon"><svg><use href="#i-news"/></svg></span>Newspapers</div>
      <div class="app"><span class="app__icon"><svg><use href="#i-globe"/></svg></span>Internet</div>
      <div class="app"><span class="app__icon"><svg><use href="#i-tv"/></svg></span>TV</div>
      <div class="app"><span class="app__icon"><svg><use href="#i-clap"/></svg></span>Movies</div>
      <div class="app"><span class="app__icon"><svg><use href="#i-tablet"/></svg></span>Tablets</div>
      <div class="app"><span class="app__icon"><svg><use href="#i-radio"/></svg></span>Radio</div>
      <div class="app"><span class="app__icon"><svg><use href="#i-comic"/></svg></span>Comics</div>
      <div class="app"><span class="app__icon"><svg><use href="#i-book"/></svg></span>Books</div>
      <div class="app"><span class="app__icon"><svg><use href="#i-note"/></svg></span>Music</div>
      <div class="app"><span class="app__icon"><svg><use href="#i-share"/></svg></span>Social Media</div>
      <div class="app"><span class="app__icon"><svg><use href="#i-pad"/></svg></span>Video Games</div>
      <div class="app"><span class="app__icon"><svg><use href="#i-power"/></svg></span>Off</div>
    </div>
  </div>

  <div class="abs url footer-url">www.<b>civiclearningstudio</b>.org</div>
</section>

<!-- BACK -->
<section class="card card--back" aria-label="Postcard back: Key Questions of Media Literacy">
  <div class="abs questions-panel"></div>
  <div class="abs questions-head">KEY QUESTIONS OF MEDIA LITERACY</div>
  <ul class="questions">
    <li><span class="tick"><svg><use href="#i-tick"/></svg></span>Who is the author and what is the purpose?</li>
    <li><span class="tick"><svg><use href="#i-tick"/></svg></span>What techniques are used to attract and<br>hold your attention?</li>
    <li><span class="tick"><svg><use href="#i-tick"/></svg></span>What lifestyles, values and points of<br>view are represented?</li>
    <li><span class="tick"><svg><use href="#i-tick"/></svg></span>How might different people interpret<br>the message?</li>
    <li><span class="tick"><svg><use href="#i-tick"/></svg></span>What is omitted from the message?</li>
  </ul>

  <div class="brand brand--back">
    <div class="brand__row"><span class="brand__mark"></span><span class="brand__name">Civic Learning Studio</span></div>
    <div class="url">www.<b>civiclearningstudio</b>.org</div>
  </div>

  <div class="abs mini-phone">
    <div class="mini-phone__title">KEY QUESTIONS OF<br>MEDIA LITERACY</div>
    <div class="mini-q"><span>1</span><p>Who is the author and what is the purpose?</p></div>
    <div class="mini-q mini-q--2"><span>2</span><p>What techniques are used to attract and hold your attention?</p></div>
    <div class="mini-q mini-q--3"><span>3</span><p>What lifestyles, values and points of view are represented?</p></div>
    <div class="mini-q mini-q--4"><span>4</span><p>How might different people interpret the message?</p></div>
    <div class="mini-q"><span>5</span><p>What is omitted from the message?</p></div>
    <div class="mini-phone__brand">Civic Learning Studio<small>www.civiclearningstudio.org</small></div>
  </div>

  <div class="abs stamp"></div>
  <div class="abs addr-line" style="top:247px"></div>
  <div class="abs addr-line" style="top:306px"></div>
  <div class="abs addr-line" style="top:366px"></div>
  <div class="abs addr-line" style="top:424px"></div>
</section>

</body>
</html>
```